Business Card Design Project 4 Construction Business

I am after a creative, but sleek and simple/ clean business card design. This design will form the basis of future items and might include a logo or simply a creative way to lay out the text of my company name 'kestrel ventures'
I like the simplicity of black and white however I would also be happy to see a splash of colour introduced somehow to give the text some interest and make it stand out.
I would like a double sided card.
I am young (ish!) and professional, offering construction and project management services, what I don't want is the traditional builders type card featuring a cheesy hammer/ saw image etc.
As the company name, kestrel ventures, suggests, we focus on working closely and collaboratively together, in synergy with all stakeholders involved in the projects that we undertake
Construction

```html
<!DOCTYPE html>
<html lang="en">
<head>
<meta charset="utf-8">
<title>Kestrel Ventures – Business Card Set</title>
<link rel="stylesheet" href="https://fonts.googleapis.com/css2?family=Michroma&family=Open+Sans:wght@400&family=Exo+2:wght@300&display=swap">
<style>
  :root {
    --board-center: #9a9a9a;
    --board-edge: #3c3c3c;
    --board-frame: #2a2a2a;
    --card-black: #000000;
    --card-white: #ffffff;
    --card-border: #b9b9b9;
    --brand-blue: #1ea3cd;
    --ink: #111111;
    --ink-soft: #444444;
    --rule: #555555;
  }
  * { margin: 0; padding: 0; box-sizing: border-box; }
  html, body { width: 1200px; height: 1184px; overflow: hidden; }
  body {
    background: radial-gradient(ellipse at 50% 50%, var(--board-center) 0%, #707070 45%, var(--board-edge) 100%);
    border: 2px solid var(--board-frame);
    position: relative;
    font-family: "Open Sans", Arial, sans-serif;
  }
  .card {
    position: absolute;
    width: 515px;
    height: 294px;
    box-shadow: 0 0 18px rgba(0,0,0,0.45);
    overflow: hidden;
  }
  .card--front { left: 76px; background: var(--card-black); }
  .card--back { left: 619px; background: var(--card-white); border: 2px solid var(--card-border); }
  .row-1 { top: 97px; }
  .row-2 { top: 444px; }
  .row-3 { top: 791px; }

  .wordmark { position: absolute; display: flex; align-items: center; gap: 12px; font-family: "Michroma", sans-serif; }
  .wordmark__mark { background: currentColor; flex: none; }
  .wordmark__text { line-height: 1.05; letter-spacing: 2px; text-transform: uppercase; white-space: nowrap; }
  .wordmark__text span { display: block; }

  .card--front .wordmark { left: 78px; top: 106px; color: var(--card-white); gap: 26px; }
  .card--front .wordmark__mark { width: 62px; height: 62px; }
  .card--front .wordmark__line-1 { font-size: 33px; }
  .card--front .wordmark__line-2 { font-size: 27px; letter-spacing: 5px; }

  .card--back .wordmark { color: var(--brand-blue); }
  .card--back .wordmark__mark { width: 34px; height: 34px; }
  .card--back .wordmark__line-1 { font-size: 19px; }
  .card--back .wordmark__line-2 { font-size: 15px; letter-spacing: 4px; }
  .wordmark--right { right: 16px; top: 14px; }
  .wordmark--left { left: 14px; top: 18px; }

  .holder { position: absolute; left: 0; top: 80px; display: flex; }
  .holder__tab { width: 18px; height: 15px; background: var(--ink); margin-top: 6px; }
  .holder__main { padding-left: 7px; padding-right: 7px; border-right: 1px solid #999; text-align: right; }
  .holder__name { font-family: "Michroma", sans-serif; color: var(--brand-blue); font-size: 20px; letter-spacing: 1px; text-transform: uppercase; line-height: 1.25; white-space: nowrap; }
  .holder__phone { font-size: 11px; color: var(--ink-soft); display: flex; align-items: center; justify-content: flex-end; gap: 4px; }
  .holder__role { font-family: "Exo 2", sans-serif; font-weight: 300; font-size: 12px; color: var(--ink-soft); letter-spacing: 1px; padding-left: 7px; padding-top: 12px; }

  .holder-right { position: absolute; right: 0; top: 88px; display: flex; }
  .holder-right__text { text-align: right; padding-right: 9px; }
  .holder-right__name { font-family: "Michroma", sans-serif; color: var(--brand-blue); font-size: 21px; letter-spacing: 1px; text-transform: uppercase; line-height: 1.2; white-space: nowrap; }
  .holder-right__role { font-family: "Exo 2", sans-serif; font-weight: 300; font-size: 13px; color: var(--ink-soft); letter-spacing: 1px; line-height: 1; }
  .holder-right__bar { width: 8px; height: 37px; background: var(--brand-blue); }

  .contacts { position: absolute; list-style: none; color: var(--ink-soft); white-space: nowrap; }
  .contacts li { display: flex; align-items: center; gap: 8px; line-height: 13.5px; }
  .contacts svg { width: 10px; height: 10px; flex: none; fill: var(--ink); }
  .contacts__indent { padding-left: 18px; }
  .contacts--ruled { left: 338px; top: 184px; border-left: 1px solid var(--rule); padding-left: 7px; font-size: 13.5px; }
  .contacts--edge { left: 350px; top: 148px; font-size: 11.5px; }
  .contacts--edge li { line-height: 12.8px; gap: 14px; }
  .contacts--edge .contacts__indent { padding-left: 24px; }
  .edge-rule { position: absolute; right: 0; top: 178px; width: 2px; height: 98px; background: var(--ink); }
  .row-3 .contacts--edge { top: 178px; }
</style>
</head>
<body>
<svg width="0" height="0" style="position:absolute" aria-hidden="true">
  <symbol id="ico-home" viewBox="0 0 10 10"><path d="M5 0.5 0 5h1.5v4.5h2.5V6.5h2v3h2.5V5H10z"/></symbol>
  <symbol id="ico-phone" viewBox="0 0 10 10"><path d="M2 0.5 3.8 2.8 2.8 4c.6 1.3 1.7 2.4 3 3l1.2-1 2.3 1.8-1.5 1.7C4.5 9 1 5.5.5 2z"/></symbol>
  <symbol id="ico-fax" viewBox="0 0 10 10"><path d="M3 0.5h4v3H3zM0.5 4h9v5.5h-9z"/></symbol>
  <symbol id="ico-mail" viewBox="0 0 10 10"><path d="M0.5 2h9v6.5h-9zM1.5 3v.4L5 5.8l3.5-2.4V3zm0 1.6v2.9h7V4.6L5 7z" fill-rule="evenodd"/></symbol>
  <symbol id="ico-web" viewBox="0 0 10 10"><circle cx="5" cy="5" r="4.5"/></symbol>
  <symbol id="ico-mobile" viewBox="0 0 10 10"><path d="M2.5 0.5h5v9h-5zM3.5 1.5v6h3v-6z" fill-rule="evenodd"/></symbol>
</svg>

<section class="card card--front row-1">
  <div class="wordmark"><span class="wordmark__mark"></span><div class="wordmark__text"><span class="wordmark__line-1">Kestrel</span><span class="wordmark__line-2">Ventures</span></div></div>
</section>
<section class="card card--back row-1">
  <div class="wordmark wordmark--right"><span class="wordmark__mark"></span><div class="wordmark__text"><span class="wordmark__line-1">Kestrel</span><span class="wordmark__line-2">Ventures</span></div></div>
  <div class="holder">
    <span class="holder__tab"></span>
    <div class="holder__main"><div class="holder__name">Marcus Hale</div><div class="holder__phone"><svg width="8" height="9"><use href="#ico-mobile"/></svg>0000-4417082</div></div>
    <div class="holder__role">Director</div>
  </div>
  <ul class="contacts contacts--ruled">
    <li><svg><use href="#ico-home"/></svg>FF-118, Oak Street</li>
    <li class="contacts__indent">Boston, USA</li>
    <li><svg><use href="#ico-phone"/></svg>0000000</li>
    <li><svg><use href="#ico-fax"/></svg>0000000</li>
    <li><svg><use href="#ico-mail"/></svg>info@kestrel.com</li>
    <li><svg><use href="#ico-web"/></svg>www.kestrel.com</li>
  </ul>
</section>

<section class="card card--front row-2">
  <div class="wordmark"><span class="wordmark__mark"></span><div class="wordmark__text"><span class="wordmark__line-1">Kestrel</span><span class="wordmark__line-2">Ventures</span></div></div>
</section>
<section class="card card--back row-2">
  <div class="wordmark wordmark--right"><span class="wordmark__mark"></span><div class="wordmark__text"><span class="wordmark__line-1">Kestrel</span><span class="wordmark__line-2">Ventures</span></div></div>
  <div class="holder">
    <span class="holder__tab"></span>
    <div class="holder__main"><div class="holder__name">Marcus Hale</div><div class="holder__phone"><svg width="8" height="9"><use href="#ico-mobile"/></svg>0000-4417082</div></div>
    <div class="holder__role">Director</div>
  </div>
  <ul class="contacts contacts--ruled">
    <li><svg><use href="#ico-home"/></svg>FF-118, Oak Street</li>
    <li class="contacts__indent">Boston, USA</li>
    <li><svg><use href="#ico-phone"/></svg>0000000</li>
    <li><svg><use href="#ico-fax"/></svg>0000000</li>
    <li><svg><use href="#ico-mail"/></svg>info@kestrel.com</li>
    <li><svg><use href="#ico-web"/></svg>www.kestrel.com</li>
  </ul>
</section>

<section class="card card--front row-3">
  <div class="wordmark"><span class="wordmark__mark"></span><div class="wordmark__text"><span class="wordmark__line-1">Kestrel</span><span class="wordmark__line-2">Ventures</span></div></div>
</section>
<section class="card card--back row-3">
  <div class="wordmark wordmark--left"><span class="wordmark__mark"></span><div class="wordmark__text"><span class="wordmark__line-1">Kestrel</span><span class="wordmark__line-2">Ventures</span></div></div>
  <div class="holder-right">
    <div class="holder-right__text"><div class="holder-right__name">Marcus Hale</div><div class="holder-right__role">Director</div></div>
    <span class="holder-right__bar"></span>
  </div>
  <ul class="contacts contacts--edge">
    <li><svg><use href="#ico-home"/></svg>FF-118, Oak Street</li>
    <li class="contacts__indent">Boston, USA</li>
    <li><svg><use href="#ico-mobile"/></svg>0000-4417082</li>
    <li><svg><use href="#ico-phone"/></svg>0000000</li>
    <li><svg><use href="#ico-fax"/></svg>0000000</li>
    <li><svg><use href="#ico-mail"/></svg>info@kestrel.com</li>
    <li><svg><use href="#ico-web"/></svg>www.kestrel.com</li>
  </ul>
  <span class="edge-rule"></span>
</section>
</body>
</html>
```